Business Card Design and Stationary design for consulting firm

Harbourline Sourcing are looking for a new business card design and a design for their A4 letterhead / A4 invoices.

We are seeking to heavily increase our brand awareness and require a business card that's professional in appearance but also shows flare and innovation. A card design that people will remember.

About Us
Harbourline Sourcing are `The Sourcing Crew’.
Our mission is to be one of Australia’s greatest companies. Our aim is to help our customers achieve the best result from their purchasing experience.

Our Requirement:
• IMPACT! IMPACT! IMPACT!
• BUSINESS & PROFESSIONAL LOOKING

• Our business colours are orange, blue and green (See the logo attached).

We have provided an Art Design specification (attached) that needs to be followed for you to win the design. This also has the font, which is used on the logo.

We are after a two sided business card

Side One should have the:
The company Logo
The Sourcing Crew
www.harbourlinesourcing.com.au
Procure | Personnel | Probity & Privacy
Sydney | Melbourne | Adelaide | Brisbane

Side Two
Logo (optional)
Harbourline Sourcing (optional)
Employee details (details listed below)

The above format is our preferred option, but if you think you can come up with something better, feel free to put it forward.

We are leaving the design up to you, but it must incorporate the logo.

We will need a template that we can change the employee details on, as we will be adding more staff over the coming months.

The details below are for one employee per card with the same design.
------------------------

Employee Details:

Marcus Del Arroyo MBA, MMgmtStratProc
Principal Consultant
0491 372 618
Marcus@harbourlinesourcing.com.au

Brianna Tolley
Consulting Manager
0462 915 308
Brianna@harbourlinesourcing.com.au

Our website is www.harbourlinesourcing.com.au

The Letterhead / invoice needs to incorporate:
the company Logo
The Sourcing Crew
Sydney | Melbourne | Adelaide | Brisbane but otherwise the design is over to you.

This file needs to be delivered in word format as other detail will be added to the documents.

We look forward to you award winning designs. If you require any further information please feel free to contact us.

Regards
Harbourline Sourcing

Target Market(s)

Our Target market is companies with 80+ employees. The market we segment is heavily male based, between the ages of 35-55 years of age.

Industry/Entity Type

Consulting

Contact Information for Business Card

See Project Description

Font styles to use
Other font styles liked:
• See Art Specification

Requirements
Must have
• Company Colours, See Project Description
Should not have
• Be outside the Art specification guidelines

```html
<!DOCTYPE html>
<html lang="en">
<head>
<meta charset="utf-8">
<title>Harbourline Sourcing – Business Card</title>
<link href="https://fonts.googleapis.com/css2?family=Open+Sans:wght@400;600;700&display=swap" rel="stylesheet">
<style>
  :root {
    --stage: #5a3a3a;
    --card-white: #ffffff;
    --ink: #2b2b2b;
    --ink-soft: #4a4a4a;
    --brand-green: #3fae3c;
    --green-a: #8cc63f;
    --green-b: #5aa83a;
    --brand-blue: #1f8fd6;
    --blue-top: #24a4df;
    --blue-bottom: #1271be;
    --orange-a: #f9a23a;
    --orange-b: #f26b22;
    --white: #ffffff;
  }
  * { box-sizing: border-box; margin: 0; padding: 0; }
  html, body { width: 1200px; height: 1200px; overflow: hidden; }
  body {
    background: var(--stage);
    font-family: "Open Sans", sans-serif;
    position: relative;
  }
  .card {
    position: absolute;
    left: 185px;
    width: 830px;
    height: 472px;
    box-shadow: 0 4px 12px rgba(0,0,0,.35);
    overflow: hidden;
  }
  /* Front */
  .card-front { top: 108px; background: var(--card-white); }
  .brand-mark {
    position: absolute;
    right: 48px;
    top: 120px;
    display: flex;
    align-items: center;
    gap: 12px;
  }
  .brand-dot {
    width: 22px; height: 22px; border-radius: 50%;
    background: var(--brand-blue);
  }
  .brand-name {
    font-size: 30px;
    font-weight: 600;
    color: var(--ink-soft);
    letter-spacing: .5px;
  }
  .person { position: absolute; left: 46px; top: 240px; }
  .person-name { font-size: 30px; font-weight: 400; color: var(--ink); line-height: 1.15; }
  .person-quals { font-size: 20px; color: var(--ink); margin-top: 2px; }
  .person-role { font-size: 21px; color: var(--brand-green); margin-top: 2px; }
  .contact { position: absolute; left: 42px; top: 356px; }
  .contact-row {
    display: flex; align-items: center; gap: 14px;
    font-size: 21px; color: var(--ink); height: 30px;
  }
  .contact-row svg { width: 22px; height: 22px; flex: none; }
  .card-footer { position: absolute; left: 0; bottom: 0; width: 830px; height: 40px; display: flex; align-items: flex-end; }
  .footer-green { width: 400px; height: 14px; background: linear-gradient(90deg, var(--green-a), var(--green-b)); }
  .footer-blue { width: 30px; height: 40px; background: var(--brand-blue); }
  .footer-web {
    flex: 1; height: 40px;
    background: linear-gradient(90deg, var(--orange-a), var(--orange-b));
    color: var(--white); font-size: 20px;
    display: flex; align-items: center; justify-content: flex-end;
    padding-right: 30px;
  }
  /* Back */
  .card-back {
    top: 618px;
    background: linear-gradient(180deg, var(--blue-top), var(--blue-bottom));
    color: var(--white);
    text-align: center;
  }
  .back-mark {
    position: absolute; left: 0; right: 0; top: 150px;
    display: flex; flex-direction: column; align-items: center; gap: 18px;
  }
  .back-mark .brand-dot { width: 56px; height: 56px; background: var(--white); }
  .back-mark .brand-name { color: var(--white); font-size: 40px; }
  .services { position: absolute; left: 0; right: 0; top: 316px; font-size: 22px; line-height: 28px; }
  .back-web { position: absolute; left: 0; right: 0; top: 428px; font-size: 21px; }
  .back-web strong { font-weight: 700; }
</style>
</head>
<body>
  <section class="card card-front">
    <div class="brand-mark">
      <span class="brand-dot"></span>
      <span class="brand-name">Harbourline Sourcing</span>
    </div>
    <div class="person">
      <p class="person-name">Marcus Del Arroyo</p>
      <p class="person-quals">MBA, MMgmtStratProc</p>
      <p class="person-role">Principal Consultant</p>
    </div>
    <div class="contact">
      <p class="contact-row">
        <svg viewBox="0 0 22 22" aria-hidden="true"><rect x="4" y="1" width="14" height="20" rx="2" fill="var(--brand-blue)"/><rect x="6" y="3.5" width="10" height="12" fill="#fff"/><circle cx="11" cy="18" r="1.2" fill="#fff"/></svg>
        0491 372 618
      </p>
      <p class="contact-row">
        <svg viewBox="0 0 22 22" aria-hidden="true"><rect x="1" y="4" width="20" height="14" fill="var(--brand-blue)"/><path d="M2 5 L11 12 L20 5 M2 17 L8.5 10.5 M20 17 L13.5 10.5" stroke="#fff" stroke-width="1.4" fill="none"/></svg>
        Marcus@harbourlinesourcing.com.au
      </p>
    </div>
    <div class="card-footer">
      <span class="footer-green"></span>
      <span class="footer-blue"></span>
      <p class="footer-web">www.harbourlinesourcing.com.au</p>
    </div>
  </section>

  <section class="card card-back">
    <div class="back-mark">
      <span class="brand-dot"></span>
      <span class="brand-name">Harbourline Sourcing</span>
    </div>
    <div class="services">
      <p>Procure | Personnel | Probity &amp; Privacy</p>
      <p>Sydney | Melbourne | Adelaide | Brisbane</p>
    </div>
    <p class="back-web">www.<strong>harbourlinesourcing</strong>.com.au</p>
  </section>
</body>
</html>
```